Etiketten für Honig
Wir können es nicht in Worte fassen wie dankbar wir sind mit unserem Einzigartigen Design was uns Wenda die Designerin entworfen hat und unserem schönen spitzen Logo - einfach einmalig. Haben bei beiden Projekten wo Wenda mitgewirkt hat Sie als Gewinnerin ???? gekrönt Umsetzung - Geschmack - Talent Sie setzt alles so schnell um - unkompliziert und denkt selber mit, in allen Punkten wo man selber übersieht Wenda ist sehr zu empfehlen der nach etwas besonders auf der Suche ist. Danke Wenda mehr als Danke ????
Aufgabenstellung
Hallo Ihr lieben
Produktetiketten
Vorderseite
-Markenlogo ist derzeit auch bei Entwurfsplatz in Bearbeitung - mit einem Preisgeld
TERAMILO Spain
-100% Artisan Naturbelassen
Honig aus Andalusien
Sortenamen - zuerst auf Deutsch dann spanisch noch
100% Origen España
Sehr wichtig
Miel de Flores
- Berg Honig
- Miel de Monte -
- Eucalyptus Honig
- Miel de eucalipto
- Thymian Honig
- Miel Tomillo
- KastanienHonig
- Miel de castaño
- Orangenblütenhonig
- Miel azahar
Rosmarin Honig
- Miel Romero
AvocadoHonig
- Miel de Aguacate
Blütenpollen
- Bee Pollen - siehe Beispiel - Fotos
Das ist für den Mix:
Orangenblütenhonig
mit Blüten-Pollen, Gelée Royal &Propolis
Siehe Foto
Der Avocado Honig ist sehr sehr dunkel
Wenn Folie dann so das es sehr betont wird wie bei Vexa-Rino
Wenn Blüten verwendet wird denkt daran
Es sind Die Blüten von wo die Honigsorten - Geschmack entsteht
Rückseite
Abfülldatum /verfalldatum
Wird mit einer stanze drauf gemacht
Freilassen
Herkunft und Anschrift
✅100% Purer Andalusischer Honig
✅Garantiert ohne chemie
✅Abfüllung& Verpackung bei niedrigen Temperaturen & erhaltene Nährstoffe
✅ungefiltert
✅Winter nicht zugefüttert
Honig gilt als Rohkost und ist daher für Kleinkinder unter 12 Monate ungeeignet
Naturbelassener Honig kann im Laufe der Zeit kristallisieren und bei max. 40° C im Wasserbad wieder verflüssigt werden.
Wir hatten an einer no Label Ettiket gedacht
Bedeutet durchsichtige Folie
Siegelverschluss müsste dann an der Seite sein in Papierform
Die LOSnummer und ablaufdatum da drauf gestanzt werden
Könnt es bei Klebwerk.de ansehen
Und Anhang Fotos
Oder auch Baumwolle Papier da kann es i..

```html
<!DOCTYPE html>
<html lang="de">
<head>
<meta charset="utf-8">
<title>TERAMILO Honig – Etiketten</title>
<link rel="stylesheet" href="https://fonts.googleapis.com/css2?family=Josefin+Sans:wght@400;600;700&family=Permanent+Marker&display=swap">
<style>
  :root {
    --page: #f2f2f0;
    --paper: #fdf6e6;
    --ink: #2b2622;
    --strip: #2a2725;
    --sans: "Josefin Sans", sans-serif;
    --marker: "Permanent Marker", cursive;
  }
  * { box-sizing: border-box; margin: 0; padding: 0; }
  html, body { width: 1200px; height: 4056px; overflow: hidden; background: var(--page); }
  body { position: relative; font-family: var(--sans); color: var(--ink); }

  .variety { position: absolute; left: 0; width: 1200px; height: 556px; }

  .seal { position: absolute; left: 507px; top: 138px; width: 196px; height: 196px; z-index: 3; }
  .seal-strip {
    position: absolute; left: 583px; top: 300px; width: 44px; height: 164px;
    background: var(--strip); z-index: 2;
    display: flex; align-items: flex-end; justify-content: center; padding-bottom: 36px;
  }
  .seal-strip span {
    display: block; transform: rotate(-90deg); white-space: nowrap;
    color: #fff; font-size: 8px; letter-spacing: 2px; font-weight: 600;
    width: 12px; text-align: center;
  }

  .label {
    position: absolute; top: 468px; width: 276px; height: 194px;
    background: var(--paper); z-index: 1;
  }
  .label--info { left: 166px; padding: 20px 22px 0 40px; }
  .label--front { left: 468px; text-align: center; overflow: hidden; }
  .label--back { left: 770px; padding: 20px 22px 0 36px; }

  .info-title { font-size: 10px; font-weight: 700; letter-spacing: .5px; margin-bottom: 3px; }
  .info-text { font-size: 6px; line-height: 1.4; margin-bottom: 5px; text-transform: uppercase; max-width: 200px; }
  .info-weight { position: absolute; left: 40px; bottom: 22px; display: flex; align-items: baseline; gap: 6px; }
  .info-weight small { font-size: 6px; font-weight: 600; }
  .info-weight strong { font-size: 18px; font-weight: 700; }

  .front-art {
    position: absolute; left: 12px; top: 6px; width: 252px; height: 150px;
    background: radial-gradient(ellipse at center, var(--accent) 0%, transparent 70%);
    opacity: .45;
  }
  .front-claim { position: relative; margin-top: 50px; font-size: 8px; font-weight: 700; letter-spacing: .3px; }
  .front-name {
    position: relative; font-family: var(--marker); font-weight: 400;
    font-size: var(--name-size, 31px); line-height: 1; margin-top: 8px; color: var(--ink);
    white-space: nowrap;
  }
  .front-sub { position: relative; margin-top: 8px; font-size: 8px; font-weight: 700; }

  .back-title { font-size: 10px; font-weight: 700; margin-bottom: 8px; }
  .back-list { list-style: none; font-size: 6px; text-transform: uppercase; line-height: 1.3; }
  .back-list li { display: flex; gap: 5px; margin-bottom: 5px; max-width: 150px; }
  .back-list svg { flex: 0 0 8px; width: 8px; height: 8px; }
  .back-brand { position: absolute; left: 36px; bottom: 20px; display: flex; gap: 6px; align-items: center; }
  .back-brand .dot { width: 30px; height: 30px; border-radius: 50%; border: 1.5px solid var(--ink); }
  .back-brand strong { font-size: 9px; letter-spacing: 2px; display: block; }
  .back-brand small { font-size: 5px; line-height: 1.3; display: block; }
  .stamp-field { position: absolute; right: 40px; top: 20px; width: 38px; height: 150px; background: #fff; }
  .stamp-caption {
    position: absolute; right: 24px; bottom: 24px; font-size: 4.5px; font-weight: 600;
    writing-mode: vertical-rl; transform: rotate(180deg); white-space: nowrap;
  }
</style>
</head>
<body>

<svg width="0" height="0" style="position:absolute" aria-hidden="true">
  <defs>
    <path id="ring-top" d="M20,100 A80,80 0 0 1 180,100"/>
    <path id="ring-bottom" d="M178,100 A78,78 0 0 1 22,100"/>
    <symbol id="seal" viewBox="0 0 200 200">
      <circle cx="100" cy="100" r="96" fill="#fdf6e6" stroke="#2b2622" stroke-width="2.5"/>
      <circle cx="100" cy="100" r="62" fill="none" stroke="#2b2622" stroke-width="1.5"/>
      <text font-family="Josefin Sans, sans-serif" font-size="11" font-weight="600" letter-spacing="2.5" fill="#2b2622">
        <textPath href="#ring-top" startOffset="50%" text-anchor="middle">100% HONIG AUS SPANIEN</textPath>
      </text>
      <text font-family="Josefin Sans, sans-serif" font-size="11" font-weight="600" letter-spacing="2.5" fill="#2b2622">
        <textPath href="#ring-bottom" startOffset="50%" text-anchor="middle">100% MIEL ORIGEN ESPAÑA</textPath>
      </text>
      <circle cx="100" cy="88" r="14" fill="none" stroke="#2b2622" stroke-width="1.5"/>
      <text x="100" y="124" text-anchor="middle" font-family="Josefin Sans, sans-serif" font-size="10" font-weight="700" letter-spacing="2" fill="#2b2622">TERAMILO</text>
    </symbol>
    <symbol id="tick" viewBox="0 0 10 10">
      <rect x="0.5" y="0.5" width="9" height="9" rx="2" fill="none" stroke="#2b2622"/>
      <path d="M2.5 5 L4.5 7 L8 2.5" fill="none" stroke="#2b2622" stroke-width="1.2"/>
    </symbol>
  </defs>
</svg>

<!-- Berg -->
<section class="variety" style="top:0;--accent:#c9b8a3">
  <svg class="seal" aria-label="Siegel TERAMILO"><use href="#seal"/></svg>
  <div class="seal-strip"><span>MIEL ARTISAN</span></div>
  <article class="label label--info">
    <h2 class="info-title">BERG HONIG</h2>
    <p class="info-text">Dieser Honig aus den Bergen Andalusiens besticht durch sein einzigartiges Aroma und seine Cremigkeit.</p>
    <p class="info-text">Naturbelassener Honig kann im Laufe der Zeit kristallisieren und bei max. 40°C im Wasserbad wieder verflüssigt werden.</p>
    <p class="info-text">Trocken und vor Wärme geschützt lagern</p>
    <p class="info-text">Für Kinder unter 12 Monaten nicht geeignet</p>
    <p class="info-text">Ursprungsland Spanien</p>
    <div class="info-weight"><small>INHALT</small><strong>℮300g</strong></div>
  </article>
  <article class="label label--front">
    <div class="front-art" role="img" aria-label="Geometrische Biene in Beige"></div>
    <p class="front-claim">100% PURES ANDALUSIEN</p>
    <h1 class="front-name">BERG<br>HONIG</h1>
    <p class="front-sub">MIEL DE MONTE</p>
  </article>
  <article class="label label--back">
    <h3 class="back-title">TERAMILO QUALITÄT</h3>
    <ul class="back-list">
      <li><svg><use href="#tick"/></svg>100% purer andalusischer Honig</li>
      <li><svg><use href="#tick"/></svg>Garantiert ohne Chemie</li>
      <li><svg><use href="#tick"/></svg>Ungefiltert und naturbelassen</li>
      <li><svg><use href="#tick"/></svg>Ohne Zufütterung im Winter</li>
      <li><svg><use href="#tick"/></svg>Abfüllung &amp; Verpackung bei niedrigen Temperaturen</li>
    </ul>
    <div class="back-brand"><span class="dot"></span><div><strong>TERAMILO</strong><small>Musterstraße 11, 12345 Musterstadt<br>kontakt@teramilo.example<br>+34 000 5550182</small></div></div>
    <div class="stamp-field"></div>
    <p class="stamp-caption">LOSNUMMER: · MINDESTENS HALTBAR BIS:</p>
  </article>
</section>

<!-- Orangenblüten -->
<section class="variety" style="top:556px;--accent:#f2b33d;--name-size:25px">
  <svg class="seal" aria-label="Siegel TERAMILO"><use href="#seal"/></svg>
  <div class="seal-strip"><span>MIEL ARTISAN</span></div>
  <article class="label label--info">
    <h2 class="info-title">ORANGENBLÜTEN HONIG</h2>
    <p class="info-text">Dieser Honig aus den Orangenblüten Andalusiens besticht durch sein einzigartiges Aroma.</p>
    <p class="info-text">Naturbelassener Honig kann im Laufe der Zeit kristallisieren und bei max. 40°C im Wasserbad wieder verflüssigt werden.</p>
    <p class="info-text">Trocken und vor Wärme geschützt lagern</p>
    <p class="info-text">Für Kinder unter 12 Monaten nicht geeignet</p>
    <p class="info-text">Ursprungsland Spanien</p>
    <div class="info-weight"><small>INHALT</small><strong>℮300g</strong></div>
  </article>
  <article class="label label--front">
    <div class="front-art" role="img" aria-label="Geometrische Biene in Orange"></div>
    <p class="front-claim">100% PURES ANDALUSIEN</p>
    <h1 class="front-name">ORANGENBLÜTEN<br>HONIG</h1>
    <p class="front-sub">MIEL DE AZAHAR</p>
  </article>
  <article class="label label--back">
    <h3 class="back-title">TERAMILO QUALITÄT</h3>
    <ul class="back-list">
      <li><svg><use href="#tick"/></svg>100% purer andalusischer Honig</li>
      <li><svg><use href="#tick"/></svg>Garantiert ohne Chemie</li>
      <li><svg><use href="#tick"/></svg>Ungefiltert und naturbelassen</li>
      <li><svg><use href="#tick"/></svg>Ohne Zufütterung im Winter</li>
      <li><svg><use href="#tick"/></svg>Abfüllung &amp; Verpackung bei niedrigen Temperaturen</li>
    </ul>
    <div class="back-brand"><span class="dot"></span><div><strong>TERAMILO</strong><small>Musterstraße 11, 12345 Musterstadt<br>kontakt@teramilo.example<br>+34 000 5550182</small></div></div>
    <div class="stamp-field"></div>
    <p class="stamp-caption">LOSNUMMER: · MINDESTENS HALTBAR BIS:</p>
  </article>
</section>

<!-- Avocado -->
<section class="variety" style="top:1112px;--accent:#b9bf5a">
  <svg class="seal" aria-label="Siegel TERAMILO"><use href="#seal"/></svg>
  <div class="seal-strip"><span>MIEL ARTISAN</span></div>
  <article class="label label--info">
    <h2 class="info-title">AVOCADO HONIG</h2>
    <p class="info-text">Dieser Honig aus Avocadoblüten besticht durch sein einzigartiges Aroma und seine Cremigkeit.</p>
    <p class="info-text">Naturbelassener Honig kann im Laufe der Zeit kristallisieren und bei max. 40°C im Wasserbad wieder verflüssigt werden.</p>
    <p class="info-text">Trocken und vor Wärme geschützt lagern</p>
    <p class="info-text">Für Kinder unter 12 Monaten nicht geeignet</p>
    <p class="info-text">Ursprungsland Spanien</p>
    <div class="info-weight"><small>INHALT</small><strong>℮300g</strong></div>
  </article>
  <article class="label label--front">
    <div class="front-art" role="img" aria-label="Geometrische Biene in Olivgrün"></div>
    <p class="front-claim">100% PURES ANDALUSIEN</p>
    <h1 class="front-name">AVOCADO<br>HONIG</h1>
    <p class="front-sub">MIEL DE AGUACATE</p>
  </article>
  <article class="label label--back">
    <h3 class="back-title">TERAMILO QUALITÄT</h3>
    <ul class="back-list">
      <li><svg><use href="#tick"/></svg>100% purer andalusischer Honig</li>
      <li><svg><use href="#tick"/></svg>Garantiert ohne Chemie</li>
      <li><svg><use href="#tick"/></svg>Ungefiltert und naturbelassen</li>
      <li><svg><use href="#tick"/></svg>Ohne Zufütterung im Winter</li>
      <li><svg><use href="#tick"/></svg>Abfüllung &amp; Verpackung bei niedrigen Temperaturen</li>
    </ul>
    <div class="back-brand"><span class="dot"></span><div><strong>TERAMILO</strong><small>Musterstraße 11, 12345 Musterstadt<br>kontakt@teramilo.example<br>+34 000 5550182</small></div></div>
    <div class="stamp-field"></div>
    <p class="stamp-caption">LOSNUMMER: · MINDESTENS HALTBAR BIS:</p>
  </article>
</section>

<!-- Eukalyptus -->
<section class="variety" style="top:1668px;--accent:#8ec9c4;--name-size:28px">
  <svg class="seal" aria-label="Siegel TERAMILO"><use href="#seal"/></svg>
  <div class="seal-strip"><span>MIEL ARTISAN</span></div>
  <article class="label label--info">
    <h2 class="info-title">EUKALYPTUS HONIG</h2>
    <p class="info-text">Dieser Honig aus Eukalyptusblüten besticht durch sein einzigartiges Aroma und seine Cremigkeit.</p>
    <p class="info-text">Naturbelassener Honig kann im Laufe der Zeit kristallisieren und bei max. 40°C im Wasserbad wieder verflüssigt werden.</p>
    <p class="info-text">Trocken und vor Wärme geschützt lagern</p>
    <p class="info-text">Für Kinder unter 12 Monaten nicht geeignet</p>
    <p class="info-text">Ursprungsland Spanien</p>
    <div class="info-weight"><small>INHALT</small><strong>℮300g</strong></div>
  </article>
  <article class="label label--front">
    <div class="front-art" role="img" aria-label="Geometrische Biene in Türkis"></div>
    <p class="front-claim">100% PURES ANDALUSIEN</p>
    <h1 class="front-name">EUKALYPTUS<br>HONIG</h1>
    <p class="front-sub">MIEL DE EUCALIPTO</p>
  </article>
  <article class="label label--back">
    <h3 class="back-title">TERAMILO QUALITÄT</h3>
    <ul class="back-list">
      <li><svg><use href="#tick"/></svg>100% purer andalusischer Honig</li>
      <li><svg><use href="#tick"/></svg>Garantiert ohne Chemie</li>
      <li><svg><use href="#tick"/></svg>Ungefiltert und naturbelassen</li>
      <li><svg><use href="#tick"/></svg>Ohne Zufütterung im Winter</li>
      <li><svg><use href="#tick"/></svg>Abfüllung &amp; Verpackung bei niedrigen Temperaturen</li>
    </ul>
    <div class="back-brand"><span class="dot"></span><div><strong>TERAMILO</strong><small>Musterstraße 11, 12345 Musterstadt<br>kontakt@teramilo.example<br>+34 000 5550182</small></div></div>
    <div class="stamp-field"></div>
    <p class="stamp-caption">LOSNUMMER: · MINDESTENS HALTBAR BIS:</p>
  </article>
</section>

<!-- Thymian -->
<section class="variety" style="top:2224px;--accent:#a79ad0">
  <svg class="seal" aria-label="Siegel TERAMILO"><use href="#seal"/></svg>
  <div class="seal-strip"><span>MIEL ARTISAN</span></div>
  <article class="label label--info">
    <h2 class="info-title">THYMIAN HONIG</h2>
    <p class="info-text">Dieser Honig aus Thymianblüten besticht durch sein einzigartiges Aroma und seine Cremigkeit.</p>
    <p class="info-text">Naturbelassener Honig kann im Laufe der Zeit kristallisieren und bei max. 40°C im Wasserbad wieder verflüssigt werden.</p>
    <p class="info-text">Trocken und vor Wärme geschützt lagern</p>
    <p class="info-text">Für Kinder unter 12 Monaten nicht geeignet</p>
    <p class="info-text">Ursprungsland Spanien</p>
    <div class="info-weight"><small>INHALT</small><strong>℮300g</strong></div>
  </article>
  <article class="label label--front">
    <div class="front-art" role="img" aria-label="Geometrische Biene in Lavendel"></div>
    <p class="front-claim">100% PURES ANDALUSIEN</p>
    <h1 class="front-name">THYMIAN<br>HONIG</h1>
    <p class="front-sub">MIEL DE TOMILLO</p>
  </article>
  <article class="label label--back">
    <h3 class="back-title">TERAMILO QUALITÄT</h3>
    <ul class="back-list">
      <li><svg><use href="#tick"/></svg>100% purer andalusischer Honig</li>
      <li><svg><use href="#tick"/></svg>Garantiert ohne Chemie</li>
      <li><svg><use href="#tick"/></svg>Ungefiltert und naturbelassen</li>
      <li><svg><use href="#tick"/></svg>Ohne Zufütterung im Winter</li>
      <li><svg><use href="#tick"/></svg>Abfüllung &amp; Verpackung bei niedrigen Temperaturen</li>
    </ul>
    <div class="back-brand"><span class="dot"></span><div><strong>TERAMILO</strong><small>Musterstraße 11, 12345 Musterstadt<br>kontakt@teramilo.example<br>+34 000 5550182</small></div></div>
    <div class="stamp-field"></div>
    <p class="stamp-caption">LOSNUMMER: · MINDESTENS HALTBAR BIS:</p>
  </article>
</section>

<!-- Kastanien -->
<section class="variety" style="top:2780px;--accent:#ec9a9a">
  <svg class="seal" aria-label="Siegel TERAMILO"><use href="#seal"/></svg>
  <div class="seal-strip"><span>MIEL ARTISAN</span></div>
  <article class="label label--info">
    <h2 class="info-title">KASTANIEN HONIG</h2>
    <p class="info-text">Dieser Honig aus Kastanienblüten besticht durch sein einzigartiges Aroma und seine Cremigkeit.</p>
    <p class="info-text">Naturbelassener Honig kann im Laufe der Zeit kristallisieren und bei max. 40°C im Wasserbad wieder verflüssigt werden.</p>
    <p class="info-text">Trocken und vor Wärme geschützt lagern</p>
    <p class="info-text">Für Kinder unter 12 Monaten nicht geeignet</p>
    <p class="info-text">Ursprungsland Spanien</p>
    <div class="info-weight"><small>INHALT</small><strong>℮300g</strong></div>
  </article>
  <article class="label label--front">
    <div class="front-art" role="img" aria-label="Geometrische Biene in Rosa"></div>
    <p class="front-claim">100% PURES ANDALUSIEN</p>
    <h1 class="front-name">KASTANIEN<br>HONIG</h1>
    <p class="front-sub">MIEL DE CASTAÑO</p>
  </article>
  <article class="label label--back">
    <h3 class="back-title">TERAMILO QUALITÄT</h3>
    <ul class="back-list">
      <li><svg><use href="#tick"/></svg>100% purer andalusischer Honig</li>
      <li><svg><use href="#tick"/></svg>Garantiert ohne Chemie</li>
      <li><svg><use href="#tick"/></svg>Ungefiltert und naturbelassen</li>
      <li><svg><use href="#tick"/></svg>Ohne Zufütterung im Winter</li>
      <li><svg><use href="#tick"/></svg>Abfüllung &amp; Verpackung bei niedrigen Temperaturen</li>
    </ul>
    <div class="back-brand"><span class="dot"></span><div><strong>TERAMILO</strong><small>Musterstraße 11, 12345 Musterstadt<br>kontakt@teramilo.example<br>+34 000 5550182</small></div></div>
    <div class="stamp-field"></div>
    <p class="stamp-caption">LOSNUMMER: · MINDESTENS HALTBAR BIS:</p>
  </article>
</section>

<!-- Rosmarin -->
<section class="variety" style="top:3336px;--accent:#9aa6d9">
  <svg class="seal" aria-label="Siegel TERAMILO"><use href="#seal"/></svg>
  <div class="seal-strip"><span>MIEL ARTISAN</span></div>
  <article class="label label--info">
    <h2 class="info-title">ROSMARIN HONIG</h2>
    <p class="info-text">Dieser Honig aus Rosmarinblüten besticht durch sein einzigartiges Aroma und seine Cremigkeit.</p>
    <p class="info-text">Naturbelassener Honig kann im Laufe der Zeit kristallisieren und bei max. 40°C im Wasserbad wieder verflüssigt werden.</p>
    <p class="info-text">Trocken und vor Wärme geschützt lagern</p>
    <p class="info-text">Für Kinder unter 12 Monaten nicht geeignet</p>
    <p class="info-text">Ursprungsland Spanien</p>
    <div class="info-weight"><small>INHALT</small><strong>℮300g</strong></div>
  </article>
  <article class="label label--front">
    <div class="front-art" role="img" aria-label="Geometrische Biene in Blau"></div>
    <p class="front-claim">100% PURES ANDALUSIEN</p>
    <h1 class="front-name">ROSMARIN<br>HONIG</h1>
    <p class="front-sub">MIEL DE ROMERO</p>
  </article>
  <article class="label label--back">
    <h3 class="back-title">TERAMILO QUALITÄT</h3>
    <ul class="back-list">
      <li><svg><use href="#tick"/></svg>100% purer andalusischer Honig</li>
      <li><svg><use href="#tick"/></svg>Garantiert ohne Chemie</li>
      <li><svg><use href="#tick"/></svg>Ungefiltert und naturbelassen</li>
      <li><svg><use href="#tick"/></svg>Ohne Zufütterung im Winter</li>
      <li><svg><use href="#tick"/></svg>Abfüllung &amp; Verpackung bei niedrigen Temperaturen</li>
    </ul>
    <div class="back-brand"><span class="dot"></span><div><strong>TERAMILO</strong><small>Musterstraße 11, 12345 Musterstadt<br>kontakt@teramilo.example<br>+34 000 5550182</small></div></div>
    <div class="stamp-field"></div>
    <p class="stamp-caption">LOSNUMMER: · MINDESTENS HALTBAR BIS:</p>
  </article>
</section>

</body>
</html>
```